Business cards — need something that creates “wow” factor

Need a sleek and clean looking business card. Something that is clear and consise. These business cards are for my painting business and hundreds will be placed in the Dallas area between all Halbrook Fennimore paint stored. These card really need to stick out! Open to any and all ideas...

Target Market(s)

Residential clientele

Industry/Entity Type

Painting

Contact Information for Business Card

Galvin Otterly
Owner

582.316.0478

Web: Brightoakfinishes.com (still under construction)
Brightoakfinishes@mailbay.com

Font styles to use
Sans Serif

Colors

Designer to choose colors to be used in the design.

Requirements
Must have
• My name, number, website, email, Facebook
• and “100% customer satisfaction guaranteed”
• Facebook.com/Brightoakfinishes/
Nice to have
• Listed services
• Interior/exterior painting
• Drywall repair/texture
• Fence staining/refinishing
• Concrete staining
• Epoxy flooring
• Pressure washing

```html
<!DOCTYPE html>
<html lang="en">
<head>
<meta charset="utf-8">
<title>Bright Oak Finishes — Business Card</title>
<link href="https://fonts.googleapis.com/css2?family=Roboto:ital,wght@0,400;0,500;0,700;1,700&family=Roboto+Condensed:wght@700&display=swap" rel="stylesheet">
<style>
  :root {
    --backdrop: #e4e1dc;
    --card-light: #f4f4f3;
    --card-dark: #000000;
    --ink: #1a1a1a;
    --ink-soft: #4a4a4a;
    --accent-blue: #3a8fb0;
    --white: #ffffff;
    --dot-red: #b8222c;
    --dot-orange-red: #e5442b;
    --dot-orange: #f29020;
    --dot-green: #7cc242;
    --dot-blue: #3a9fc0;
    --dot-purple: #8a4aa0;
    --decor-dark: #141414;
  }
  * { box-sizing: border-box; margin: 0; padding: 0; }
  html, body { width: 1200px; height: 960px; overflow: hidden; }
  body {
    background: var(--backdrop);
    font-family: "Roboto", Arial, sans-serif;
    position: relative;
  }
  .card {
    position: absolute;
    width: 600px;
    height: 342px;
    box-shadow: 0 2px 6px rgba(0,0,0,0.25);
    overflow: hidden;
  }
  .card--front { left: 314px; top: 113px; background: var(--card-light); }
  .card--back { left: 311px; top: 472px; background: var(--card-dark); }

  .brand {
    position: absolute;
    left: 48px; top: 96px;
    display: flex; align-items: center; gap: 10px;
  }
  .brand__mark {
    width: 14px; height: 14px; border-radius: 50%;
    background: var(--accent-blue);
  }
  .brand__name {
    font-size: 26px; font-weight: 500; color: var(--ink);
    letter-spacing: 0.5px;
  }

  .person { position: absolute; left: 47px; top: 237px; }
  .person__name {
    font-family: "Roboto Condensed", "Roboto", sans-serif;
    font-weight: 700; font-size: 22px; color: var(--accent-blue);
    text-transform: uppercase; letter-spacing: 0.2px;
  }
  .person__title {
    font-size: 15px; font-weight: 500; color: var(--ink);
    text-transform: uppercase; margin-top: 2px;
  }

  .contacts { position: absolute; left: 330px; top: 202px; list-style: none; }
  .contacts__item {
    display: flex; align-items: center; gap: 7px;
    font-size: 14.5px; color: var(--ink-soft); height: 19px;
  }
  .contacts__icon { width: 12px; height: 12px; flex: none; fill: var(--accent-blue); }
  .contacts__square { width: 11px; height: 11px; background: var(--accent-blue); flex: none; margin-right: 1px; }

  .guarantee {
    position: absolute; left: 0; bottom: 0; width: 100%; height: 31px;
    background: linear-gradient(90deg, #c4202e 0%, #e33b2c 22%, #f2901f 42%, #c6cf3a 58%, #5fba8a 72%, #3aa0b8 86%, #4a4b8f 100%);
    color: var(--white); font-weight: 700; font-style: italic; font-size: 16px;
    display: flex; align-items: center; justify-content: center;
    padding-left: 16px;
  }

  .back-decor {
    position: absolute; left: 68px; top: 0; width: 440px; height: 342px;
    background: radial-gradient(ellipse at 60% 40%, var(--decor-dark) 0%, rgba(0,0,0,0) 70%);
  }
  .services {
    position: absolute; left: 0; top: 68px; width: 100%;
    list-style: none; text-align: center;
  }
  .services__item {
    color: var(--white); font-size: 21px; height: 34px; line-height: 34px;
  }
  .services__dot {
    display: inline-block; width: 8px; height: 8px; border-radius: 50%;
    margin-right: 10px; vertical-align: middle; position: relative; top: -2px;
  }
  .dot--red { background: var(--dot-red); }
  .dot--orange-red { background: var(--dot-orange-red); }
  .dot--orange { background: var(--dot-orange); }
  .dot--green { background: var(--dot-green); }
  .dot--blue { background: var(--dot-blue); }
  .dot--purple { background: var(--dot-purple); }
</style>
</head>
<body>
  <section class="card card--front">
    <div class="brand">
      <span class="brand__mark"></span>
      <span class="brand__name">Bright Oak Finishes</span>
    </div>

    <div class="person">
      <p class="person__name">Galvin Otterly</p>
      <p class="person__title">Owner</p>
    </div>

    <ul class="contacts">
      <li class="contacts__item">
        <svg class="contacts__icon" viewBox="0 0 24 24"><path d="M6.6 10.8a15 15 0 0 0 6.6 6.6l2.2-2.2c.3-.3.7-.4 1-.2 1.1.4 2.3.6 3.6.6.6 0 1 .4 1 1V20c0 .6-.4 1-1 1A17 17 0 0 1 3 4c0-.6.4-1 1-1h3.5c.6 0 1 .4 1 1 0 1.3.2 2.5.6 3.6.1.3 0 .7-.2 1z"/></svg>
        582.316.0478
      </li>
      <li class="contacts__item">
        <svg class="contacts__icon" viewBox="0 0 24 24"><path d="M2 5h20v14H2z M2 5l10 8 10-8" fill="var(--accent-blue)"/><path d="M2 6l10 7 10-7" fill="none" stroke="#f4f4f3" stroke-width="1.6"/></svg>
        Brightoakfinishes@mailbay.com
      </li>
      <li class="contacts__item">
        <svg class="contacts__icon" viewBox="0 0 24 24"><circle cx="12" cy="12" r="10"/><path d="M2 12h20M12 2c3 3 3 17 0 20M12 2c-3 3-3 17 0 20" fill="none" stroke="#f4f4f3" stroke-width="1.5"/></svg>
        Brightoakfinishes.com
      </li>
      <li class="contacts__item">
        <span class="contacts__square"></span>
        Brightoakfinishes
      </li>
    </ul>

    <div class="guarantee">100% customer satisfaction guaranteed</div>
  </section>

  <section class="card card--back">
    <div class="back-decor" role="img" aria-label="Faint state outline decoration"></div>
    <ul class="services">
      <li class="services__item"><span class="services__dot dot--red"></span>Interior/exterior painting</li>
      <li class="services__item"><span class="services__dot dot--orange-red"></span>Drywall repair/texture</li>
      <li class="services__item"><span class="services__dot dot--orange"></span>Fence staining/refinishing</li>
      <li class="services__item"><span class="services__dot dot--green"></span>Concrete staining</li>
      <li class="services__item"><span class="services__dot dot--blue"></span>Epoxy flooring</li>
      <li class="services__item"><span class="services__dot dot--purple"></span>Pressure washing</li>
    </ul>
  </section>
</body>
</html>
```